Kora_Plastering Web Design Project

Kora Plastering wants a modern looking 1 page website that clearly emphasises the 3 specialised construction services:
1. Plastering = (inside walls etc)
2. Rendering = (outside walls etc)
3. Cornicing = (inside wall and ceilings)

Kora Plastering is run by craftsmen, so be creative.

I really like http://quillnorth-example.com

The site design lends itself well to being a one pager - I like the html click thru panel (at the base above the fold) that allows reader to stay on the one page but can see see more info by tapping on the red arrows.

The site is also successful because it doesn't rely on photos - but makes the most of big headlines and client testimonials.

I could provide you with more content if you need it to achieve this kind of site.

Project Deadline Extended
Reason: Hi, we have decided to extend the deadline as we have only received ideas from one designer. We feel there is still scope to improve on the designs we have received so far. Improvements in the following areas: - design that complements the new logo design (the logo shows that KORA provide services inside and outside the house) - the design doesn't look like one of the many 'template' designs you see these days - the design does not need to use photos - if you can illustrate well as well as design website you will have an advantage! - site should look very modern / up to date We have now guaranteed payment in case designers were holding off.

Target Market(s)

Architects, interior designers, builders, home owners

Industry/Entity Type

Construction

Requirements
Must have
• Design at 1024 x 768
Website design should complement new logo - with black and ivory being dominant colours. (Logo is attached)
The site should be creative - as creativity is one of the key aspects of the service provide by Kora Plastering.
Text for the site has been provided - see pdf
Nice to have
• It's not essential to use photos. In the quick example I have attached I have sourced photos from snapverde-example.com
File #: 8302947 / File #: 40918526 / File #: 9175382. I repeat photos are not mandatory - you may prefer to use other graphical devices.
Easily coded
Modern looking design

```html
<!DOCTYPE html>
<html lang="en">
<head>
<meta charset="utf-8">
<title>Kora Plastering, Melbourne</title>
<link href="https://fonts.googleapis.com/css2?family=Michroma&family=Noto+Serif:wght@400;700&family=Arimo:wght@400;700&display=swap" rel="stylesheet">
<style>
:root{
  --header-brown:#3a2f26;
  --header-brown-dark:#2c231c;
  --nav-teal:#2aa9b5;
  --nav-teal-light:#3fc2cc;
  --ivory:#f5ecc9;
  --ivory-text:#f3ead0;
  --frame-white:#fdfcf8;
  --ink:#2b231c;
  --body-text:#3a342c;
  --gold:#7d6a33;
  --link-red:#a3201b;
  --cta-green:#6dbb3c;
  --cta-green-dark:#4f9a27;
  --footer-dark:#221c17;
  --footer-muted:#b6ada0;
}
*{box-sizing:border-box;margin:0;padding:0}
html,body{width:970px;height:1200px;overflow:hidden;background:var(--ivory)}
body{position:relative;font-family:"Noto Serif",Georgia,serif;color:var(--body-text)}
.abs{position:absolute}

.site-header{left:0;top:0;width:970px;height:115px;background:linear-gradient(180deg,var(--header-brown),var(--header-brown-dark))}
.brand{left:70px;top:24px;font-family:"Michroma",sans-serif;color:var(--ivory-text);font-size:21px;letter-spacing:6px;line-height:30px;text-transform:uppercase}
.utility-links{right:75px;top:14px;font-size:11px;color:#bfb3a3;letter-spacing:.3px}
.utility-links span{margin:0 6px}
.cta-button{left:683px;top:51px;width:205px;height:42px;border-radius:3px;background:linear-gradient(180deg,var(--cta-green),var(--cta-green-dark));border:1px solid #8fd25d;display:flex;align-items:center;padding-left:4px}
.cta-button svg{flex:none}
.cta-text{margin-left:6px;color:#fff;line-height:1}
.cta-text strong{display:block;font-size:17px;font-weight:400;letter-spacing:-.2px}
.cta-text small{display:block;font-size:8.5px;font-weight:700;margin-top:3px;color:#f1fbe6}

.main-nav{left:0;top:115px;width:970px;height:42px;background:linear-gradient(180deg,var(--nav-teal-light),var(--nav-teal));display:flex;align-items:center}
.main-nav a{color:#fff;text-decoration:none;font-size:15px;margin-right:39px}
.main-nav a.current{background:#fff;color:var(--ink);padding:4px 11px;margin-left:57px;margin-right:27px;border-radius:2px}
.nav-phone{right:32px;top:126px;color:#fff;font-size:16px;font-weight:700;letter-spacing:.3px}

.photo-frame{background:var(--frame-white);box-shadow:0 1px 3px rgba(0,0,0,.25)}
.hero{left:43px;top:182px;width:888px;height:336px}
.hero-image{left:15px;top:15px;width:857px;height:305px;background:linear-gradient(90deg,#2a2724 0%,#6f6d67 12%,#a6aba8 35%,#9fa4a3 70%,#8c8d89 100%)}
.hero-floor{left:15px;top:240px;width:857px;height:80px;background:linear-gradient(90deg,#3a2f25,#9a7a48 40%,#b48b4f 70%,#2a2622)}
.hero-caption{left:15px;top:263px;width:857px;height:57px;background:rgba(20,16,14,.55);color:#fff;font-size:15px;line-height:21px;padding:6px 11px}
.slider-arrow{width:30px;height:40px;background:#fff;border-radius:50%;display:flex;align-items:center;justify-content:center}

h2{font-family:"Michroma",sans-serif;font-weight:400;color:var(--ink)}
h2 em{font-style:normal;color:var(--gold)}
.about-title{left:46px;top:540px;font-size:23px}
.about-body{left:46px;top:575px;width:840px;font-size:12px;line-height:20px}
.read-more{left:54px;top:652px;font-size:12px;color:var(--link-red)}
.read-more svg{margin-right:6px}
.work-title{left:46px;top:703px;font-size:23px}
.work-body{left:46px;top:738px;width:585px;font-size:12px;line-height:20px}
.work-frame{left:682px;top:701px;width:211px;height:158px}
.work-image{left:15px;top:15px;width:181px;height:128px;background:linear-gradient(135deg,#3d3b38,#8a8780 55%,#c9c4b9)}
.chevron{font-size:26px;font-weight:700;color:var(--ink)}

.service-title{top:878px;font-family:"Michroma",sans-serif;font-size:30px;color:var(--ink)}
.service-frame{top:927px;height:160px}
.service-image{left:15px;top:15px;bottom:15px;right:17px;border:1px solid #8a8377}

.site-footer{left:0;top:1109px;width:970px;height:91px;background:var(--footer-dark);font-family:"Arimo",Arial,sans-serif}
.footer-email{left:60px;top:1125px;color:var(--footer-muted);font-family:"Noto Serif",serif;font-size:14px}
.footer-email span{display:block;color:#fff;font-family:"Arimo",sans-serif;font-size:11.5px;margin-top:2px}
.footer-links{left:300px;top:1126px;width:380px;text-align:center;color:#fff;font-size:11px;font-weight:700}
.footer-links span{margin:0 5px;font-weight:400}
.copyright{left:300px;top:1154px;width:380px;text-align:center;color:#fff;font-size:11px;font-weight:700}
.legal-links{left:300px;top:1174px;width:380px;text-align:center;color:#ddd;font-size:10.5px}
.legal-links span{margin:0 6px}
.social-title{left:756px;top:1122px;color:var(--footer-muted);font-family:"Noto Serif",serif;font-size:14.5px}
.social-row{left:776px;top:1151px;display:flex;gap:6px}
.social-row i{width:27px;height:27px;border-radius:50%;display:block}
</style>
</head>
<body>

<header class="abs site-header"></header>
<div class="abs brand">Kora<br>Plastering</div>
<div class="abs utility-links">Home<span>|</span>Site Map<span>|</span>Contact Us</div>
<div class="abs cta-button">
  <svg width="24" height="24" viewBox="0 0 24 24"><circle cx="12" cy="12" r="11" fill="#1e2a14"/><path d="M6 10.5h7V7l5 5-5 5v-3.5H6z" fill="#fff"/></svg>
  <div class="cta-text"><strong>CONTACT US NOW</strong><small>FOR AN OBLIGATION FREE QUOTE</small></div>
</div>

<nav class="abs main-nav">
  <a class="current" href="#">HOME</a>
  <a href="#">ABOUT US</a>
  <a href="#">SERVICES</a>
  <a href="#">OUR WORK</a>
  <a href="#">CONTACT US</a>
</nav>
<div class="abs nav-phone">TEL: 0400 318 662</div>

<section class="abs hero photo-frame">
  <div class="abs hero-image" role="img" aria-label="Modern bedroom interior with a rendered grey feature wall, low bed and potted plant"></div>
  <div class="abs hero-floor" aria-hidden="true"></div>
  <div class="abs hero-caption">We are specialists in all aspects of plastering, rendering and cornicing throughout Melbourne. We undertake residential and commercial projects of all sizes, including home renovations,</div>
  <div class="abs slider-arrow" style="left:4px;top:148px"><svg width="12" height="16" viewBox="0 0 12 16"><path d="M9 1 2 8l7 7" stroke="#222" stroke-width="3.5" fill="none"/></svg></div>
  <div class="abs slider-arrow" style="left:854px;top:148px"><svg width="12" height="16" viewBox="0 0 12 16"><path d="M3 1l7 7-7 7" stroke="#222" stroke-width="3.5" fill="none"/></svg></div>
</section>

<h2 class="abs about-title">About <em>Kora Plastering</em>, Melbourne</h2>
<p class="abs about-body">We are specialists in all aspects of plastering, rendering and cornicing throughout Melbourne.<br>We undertake residential and commercial projects of all sizes, including home renovations,new builds and specialised architectural projects.<br>We are specialists in all aspects of plastering, rendering and cornicing throughout Melbourne.<br>We undertake residential and commercial projects of all sizes, including home renovations,new builds and specialised architectural projects.</p>
<div class="abs read-more"><svg width="5" height="8" viewBox="0 0 5 8"><path d="M0 0l5 4-5 4z" fill="#a3201b"/></svg>Read More</div>

<h2 class="abs work-title">Our Work</h2>
<p class="abs work-body">We work inside and out and take pride in delivering a high quality finish across a diversity of traditional and modern styles. We're always happy to provide advice and ideas - and deliver a service that's prompt, neat and on budget.</p>
<div class="abs chevron" style="left:652px;top:752px">&lsaquo;</div>
<div class="abs work-frame photo-frame">
  <div class="abs work-image" role="img" aria-label="Hand applying plaster with a trowel and hawk"></div>
</div>
<div class="abs chevron" style="left:900px;top:752px">&rsaquo;</div>

<h2 class="abs service-title" style="left:59px">Plastering</h2>
<h2 class="abs service-title" style="left:367px;top:876px">Rendering</h2>
<h2 class="abs service-title" style="left:663px">Cornicing</h2>

<div class="abs service-frame photo-frame" style="left:47px;width:246px">
  <div class="abs service-image" role="img" aria-label="Plasterer smoothing an interior wall with a trowel" style="background:linear-gradient(135deg,#d8b7a0,#c9a48a 60%,#e7d6c7)"></div>
</div>
<div class="abs service-frame photo-frame" style="left:355px;width:247px">
  <div class="abs service-image" role="img" aria-label="Steel rendering trowel with a blue and yellow handle" style="background:#fff"></div>
</div>
<div class="abs service-frame photo-frame" style="left:651px;width:250px">
  <div class="abs service-image" role="img" aria-label="Decorative cornice where ceiling meets wall" style="background:linear-gradient(160deg,#6e6a60,#c8c3b6 45%,#e3dfd4 60%,#9a9488)"></div>
</div>

<footer class="abs site-footer"></footer>
<div class="abs footer-email">E-mail<span>info@koraplastering-example.com</span></div>
<div class="abs footer-links">Home<span>|</span>About Us<span>|</span>Services<span>|</span>Our Work<span>|</span>Site Map<span>|</span>Contact Us</div>
<div class="abs copyright">Copyright &copy; 2011 KoraPlastering-example.com All rights reserved.</div>
<div class="abs legal-links">Help / Suggestions<span>|</span>Privacy Policy<span>|</span>Terms of Conditions<span>|</span>Copyright Policy</div>
<div class="abs social-title">Stay connected with us</div>
<div class="abs social-row" aria-label="Social links">
  <i style="background:#3c5a96"></i><i style="background:#35b3e3"></i><i style="background:#e8eef3"></i><i style="background:#f08a1e"></i>
</div>

</body>
</html>
```